Chiropody and Podiatry Flyer

A6 Flyer for a Chiropody Clinic.
Need to use an existing company logo (upload available).
Flyer should promote three aspects of the practice;
1) General chiropody : Nail Cutting; Corn Removal; Ingrown Nails; Hard Skin Removal; Verruca Treatment; Diabetic Assessment; Nail Surgery.
2) Home Visits - chiropody in the comfort of your own home.
3) Biomechanical Assessments / Orthotics
Colours should comprise navy blue/green/white to complement existing logo.
Promotional Offer on flyer.

Industry/Entity Type

Clinic

```html
<!DOCTYPE html>
<html lang="en">
<head>
<meta charset="utf-8">
<title>Willowbank Clinic – Chiropody &amp; Podiatry Flyer</title>
<link rel="stylesheet" href="https://fonts.googleapis.com/css2?family=Tinos:wght@400;700&display=swap">
<style>
  :root {
    --navy: #1f2d5c;
    --green-dark: #5b7f5f;
    --green-sage: #8aa27a;
    --green-bright: #8dc263;
    --grey-text: #4a4a4a;
    --panel: #f3f4f3;
    --band-light: #e4e9dd;
    --page: #e9e9e7;
    --white: #ffffff;
  }
  * { box-sizing: border-box; margin: 0; padding: 0; }
  html, body {
    width: 916px; height: 1200px; overflow: hidden;
    background: var(--page);
    font-family: "Tinos", "Times New Roman", serif;
  }
  .canvas { position: relative; width: 916px; height: 1200px; }

  .flyer {
    position: absolute; width: 672px; height: 520px;
    background: linear-gradient(90deg, var(--white), var(--panel));
    box-shadow: 0 3px 10px rgba(0,0,0,.18);
    overflow: hidden;
  }
  .flyer--front { left: 76px; top: 66px; }
  .flyer--back  { left: 164px; top: 634px; }
  .flyer__art { position: absolute; inset: 0; width: 100%; height: 100%; }

  .badge {
    position: absolute; width: 100px; height: 100px;
    display: flex; align-items: center; justify-content: center;
    text-align: center; color: var(--green-bright);
    font-weight: 700; line-height: 1.05; transform: rotate(-14deg);
  }
  .badge--book { left: 145px; top: 264px; font-size: 21px; }
  .badge--offer { left: 371px; top: 281px; font-size: 15px; }

  /* Front */
  .intro { position: absolute; right: 16px; top: 58px; width: 420px; text-align: right; }
  .intro__title { color: var(--navy); font-size: 25px; font-weight: 700; margin-bottom: 22px; }
  .intro__text { color: var(--grey-text); font-size: 14.5px; line-height: 1.45; margin-bottom: 22px; }

  .brand {
    position: absolute; left: 400px; top: 342px; width: 230px;
    text-align: center; color: var(--navy); font-size: 26px; font-weight: 400;
    white-space: nowrap;
  }
  .contact-pill {
    position: absolute; background: var(--green-bright); color: var(--white);
    border-radius: 16px; font-size: 12.5px; letter-spacing: .4px;
    display: flex; align-items: center; justify-content: center;
  }
  .contact-pill--front { left: 428px; top: 432px; width: 206px; height: 30px; }

  /* Back */
  .services { position: absolute; left: 18px; top: 162px; width: 380px; }
  .services__title { color: var(--navy); font-size: 25px; font-weight: 700; margin-bottom: 14px; }
  .service-tag {
    display: inline-flex; align-items: center; height: 34px; padding: 0 18px;
    background: var(--green-bright); color: var(--white);
    border-radius: 17px; font-size: 15.5px;
  }
  .service-tag--small { font-size: 11px; height: 32px; padding: 0 12px; }
  .service-list {
    list-style: none; display: grid; grid-template-columns: 148px 160px;
    grid-template-rows: repeat(4, auto); grid-auto-flow: column;
    row-gap: 2px; margin: 10px 0 22px 8px;
    color: var(--grey-text); font-size: 13px;
  }
  .service-list li::before { content: "• "; }
  .service-note { color: var(--grey-text); font-size: 13px; margin: 10px 0 16px 0; }
  .contact-line {
    position: absolute; right: 18px; bottom: 16px;
    color: var(--navy); font-size: 14px; letter-spacing: .4px;
  }
</style>
</head>
<body>
<main class="canvas">

  <section class="flyer flyer--front">
    <svg class="flyer__art" viewBox="0 0 672 520">
      <defs>
        <linearGradient id="relaxGrad" x1="0" y1="0" x2="1" y2="1">
          <stop offset="0" stop-color="#c9d7e0"/>
          <stop offset=".5" stop-color="#d9b58c"/>
          <stop offset="1" stop-color="#eee7dc"/>
        </linearGradient>
        <linearGradient id="feetGrad" x1="0" y1="0" x2="1" y2="1">
          <stop offset="0" stop-color="#e9c3ad"/>
          <stop offset=".6" stop-color="#dcae97"/>
          <stop offset="1" stop-color="#f4efee"/>
        </linearGradient>
      </defs>
      <path d="M0 0 H380 C 340 70, 290 150, 200 168 C 120 182, 50 168, 0 150 Z"
            fill="url(#relaxGrad)" role="img" aria-label="Photo of a woman relaxing on a cushioned wicker lounger"/>
      <path d="M0 150 C 50 168, 120 182, 200 168 C 290 150, 340 70, 380 0 H420 C 380 100, 310 200, 200 212 C 110 222, 40 205, 0 190 Z"
            fill="var(--green-sage)"/>
      <path d="M0 248 C 80 222, 160 240, 220 288 C 300 350, 370 440, 470 520 H440 C 350 440, 280 350, 205 300 C 140 262, 70 258, 0 275 Z"
            fill="var(--green-dark)"/>
      <path d="M0 275 C 70 258, 140 262, 205 300 C 280 350, 350 440, 440 520 H0 Z"
            fill="url(#feetGrad)" role="img" aria-label="Photo of manicured feet on a towel with orchid flowers"/>
      <path d="M290 380 C 380 470, 500 490, 672 430 V520 H470 C 400 490, 340 440, 290 380 Z"
            fill="var(--green-sage)"/>
      <path d="M290 380 C 360 450, 470 482, 672 420 V430 C 500 490, 380 470, 290 380 Z"
            fill="var(--green-dark)"/>
      <g transform="translate(195 314)">
        <circle r="44" fill="var(--navy)"/>
        <circle r="46" fill="none" stroke="var(--navy)" stroke-width="8" stroke-dasharray="0 11.1" stroke-linecap="round"/>
        <circle r="37" fill="none" stroke="var(--green-bright)" stroke-width="1"/>
      </g>
    </svg>

    <div class="badge badge--book">BOOK<br>NOW!</div>

    <div class="intro">
      <h1 class="intro__title">Chiropody &amp; Podiatry</h1>
      <p class="intro__text">Willowbank Clinic is a new, vibrant,<br>complementary &amp; alternative healthcare clinic<br>in Millbrook, Kent.</p>
      <p class="intro__text">Our group of dedicated and experienced practitioners<br>aim to make our clients’ health and happiness their priority!</p>
    </div>

    <div class="brand">Willowbank Clinic</div>
    <div class="contact-pill contact-pill--front">01632 960418 | 07700 900316</div>
  </section>

  <section class="flyer flyer--back">
    <svg class="flyer__art" viewBox="0 0 672 520">
      <defs>
        <linearGradient id="skyGrad" x1="0" y1="0" x2="0" y2="1">
          <stop offset="0" stop-color="#7f9bc4"/>
          <stop offset="1" stop-color="#c6d3e2"/>
        </linearGradient>
        <linearGradient id="spaGrad" x1="0" y1="0" x2="1" y2="1">
          <stop offset="0" stop-color="#e2cfbd"/>
          <stop offset=".5" stop-color="#f0ddd0"/>
          <stop offset="1" stop-color="#fbf8f5"/>
        </linearGradient>
      </defs>
      <path d="M0 0 H672 V0 C 600 60, 520 150, 400 195 C 300 225, 180 170, 0 72 Z"
            fill="url(#skyGrad)" role="img" aria-label="Photo of a woman stretching her arms wide against a blue sky"/>
      <path d="M0 72 C 180 170, 300 225, 400 195 C 520 150, 600 60, 672 0 V40 C 600 110, 520 200, 400 232 C 290 258, 170 200, 0 100 Z"
            fill="var(--green-sage)"/>
      <path d="M672 60 C 580 140, 520 230, 480 320 C 450 390, 420 440, 400 520 H430 C 445 440, 480 380, 510 320 C 550 240, 600 170, 672 110 Z"
            fill="var(--green-dark)"/>
      <path d="M672 110 C 600 170, 550 240, 510 320 C 480 380, 445 440, 430 465 H672 Z"
            fill="url(#spaGrad)" role="img" aria-label="Photo of a smiling woman with a towel wrapped around her hair"/>
      <path d="M430 465 H672 V520 H420 Z" fill="var(--band-light)"/>
      <g transform="translate(421 331)">
        <circle r="44" fill="var(--navy)"/>
        <circle r="46" fill="none" stroke="var(--navy)" stroke-width="8" stroke-dasharray="0 11.1" stroke-linecap="round"/>
        <circle r="37" fill="none" stroke="var(--green-bright)" stroke-width="1"/>
      </g>
    </svg>

    <div class="badge badge--offer">SPECIAL<br>OFFERS!</div>

    <div class="services">
      <h2 class="services__title">SERVICES</h2>
      <span class="service-tag">General Chiropody</span>
      <ul class="service-list">
        <li>Nail Cutting</li>
        <li>Corn Removal</li>
        <li>Ingrown Nails</li>
        <li>Hard Skin Removal</li>
        <li>Verruca Treatment</li>
        <li>Diabetic Assessment</li>
        <li>Nail Surgery</li>
      </ul>
      <span class="service-tag">Home Visits</span>
      <p class="service-note">Chiropody in the comfort of your own home.</p>
      <span class="service-tag service-tag--small">Biomechanical Assessments</span>
      <p class="service-note">Orthotics</p>
    </div>

    <p class="contact-line">01632 960418 | 07700 900316</p>
  </section>

</main>
</body>
</html>
```